Stationery using new logo for pharmacy and gift shop

We need a letterhead, business card, gift voucher and possibly compliments slip design for our pharmacy and gift shop using our new logo.
The letterhead would need to be produced in both colour (purple and green) and grayscale and the business card would preferably be one-sided, but can be two-sided if this works better with the information it needs to have on it.

We would like a simple and elegant design, but not so simple that it looks like we've done it ourselves on Word. Use of our colours would be great but the letterhead would need to look good if printed on our black and white laser printer. If this is not possible then an additional version for grayscale would be needed.

We would need to receive high quality files that we can work with easily, such as pdf's for the letterhead that we can print instantly or order online as it appears on screen and business cards in jpeg and pdf so we can upload to printing sites.
We would like the vouchers in denominations of £5 and £10 in A5 size in a printable format such as PDF so that we don't have to resize.

Letterhead is for use in correspondence and invoicing to patients, surgeries, traders, customers etc.

Our preferred font is Orkney

Letterhead Info
Address
47 Fenwick Rd.
Eldermere
Northdale
CA21 4QT

Tel: (01632) 960417
Fax: (01632) 960538
Website: www.brantleyspharmacy.example
Email: patientcare@brantleyspharmacy.example

Business Card Info.
As above but email address is: rkdbrantley@mailbox.example

Voucher Info.
Small print to state that any change will be paid as a credit note.
Space for a staff member to sign, date and stamp voucher

I have quite a few logo files so please ask if you need more uploaded. Or if you need more information to improve the design then please contact me.

Target Market(s)

Both retail customers and professional colleagues

Industry/Entity Type

Pharmacy

Font styles to use
Other font styles liked:
• orkney

Colors
ffffff
9bcb3c
6b449b

Requirements
Must have
• Must be clear and legible with a professional feel. Must use the logo well and all aspects of the designs should work well together.
• Final files MUST be easy to use for non-computer specialists. I need staff to be able to pull up a letterhead template easily if they are writing a letter or raising an invoice. The business card must be in a format ready to be sent to print.
Nice to have
• Letterhead available in a word processor program like word so that letters can be sent by email as well as print or print and scan.

```html
<!DOCTYPE html>
<html lang="en">
<head>
<meta charset="utf-8">
<title>Brantley Apothecary – Business Card</title>
<link rel="stylesheet" href="https://fonts.googleapis.com/css2?family=Lato:wght@400;700&family=Roboto:wght@400&display=swap">
<style>
  :root{
    --purple:#6b449b;
    --green:#9bcb3c;
    --white:#ffffff;
    --ink:#4a4a4a;
    --stage:#ecebee;
  }
  *{box-sizing:border-box;margin:0;padding:0}
  html,body{width:1200px;height:911px;overflow:hidden;background:var(--stage)}
  .canvas{position:relative;width:1200px;height:911px}
  .card{position:absolute;width:540px;height:310px;overflow:hidden;box-shadow:0 6px 18px rgba(0,0,0,.18)}

  /* front */
  .card-front{left:50px;top:170px;background:var(--white)}
  .card-front .rail-top{position:absolute;left:0;top:0;width:92px;height:118px;background:var(--green)}
  .card-front .rail-bottom{position:absolute;left:0;top:118px;width:92px;height:192px;background:var(--purple)}
  .front-brand{position:absolute;left:118px;top:30px;font-family:"Lato",sans-serif}
  .front-brand .name{font-weight:700;font-size:27px;letter-spacing:.5px;color:var(--purple);text-transform:uppercase;white-space:nowrap}
  .tagline{font-family:"Lato",sans-serif;font-weight:400;color:var(--green);text-transform:uppercase}
  .front-brand .tagline{font-size:15px;letter-spacing:1px;margin-top:2px}
  .person{position:absolute;left:118px;top:108px;font-family:"Lato",sans-serif}
  .person .full-name{font-weight:700;font-size:19px;color:var(--purple);text-transform:uppercase}
  .person .role{font-size:13px;color:var(--green);text-transform:uppercase;margin-top:1px}
  .contact{position:absolute;left:118px;top:163px;font-family:"Roboto",sans-serif;font-size:13px;color:var(--ink);line-height:19px;white-space:nowrap}
  .icons{position:absolute;left:0;top:118px;width:92px}
  .icon{position:absolute;left:37px;width:18px;height:18px;fill:none;stroke:var(--white);stroke-width:1.6}
  .icon.solid{fill:var(--white);stroke:none}

  /* back */
  .card-back{left:610px;top:420px;background:var(--purple)}
  .back-web{position:absolute;left:34px;top:155px;transform:translate(-50%,-50%) rotate(-90deg);font-family:"Roboto",sans-serif;font-size:12px;letter-spacing:3px;color:var(--white);white-space:nowrap}
  .back-brand{position:absolute;left:40px;right:0;top:92px;display:flex;flex-direction:column;align-items:center;font-family:"Lato",sans-serif}
  .back-brand .mark{width:58px;height:58px;border:4px solid var(--white);margin-bottom:14px}
  .back-brand .name{font-weight:700;font-size:30px;letter-spacing:1px;color:var(--white);text-transform:uppercase;white-space:nowrap}
  .back-brand .tagline{font-size:17px;letter-spacing:1.5px;margin-top:2px}
</style>
</head>
<body>
<main class="canvas">

  <section class="card card-front" aria-label="Business card front">
    <div class="rail-top"></div>
    <div class="rail-bottom"></div>

    <div class="front-brand">
      <div class="name">Brantley Apothecary</div>
      <div class="tagline">Health &amp; Gifts</div>
    </div>

    <div class="person">
      <div class="full-name">Owen Hartley</div>
      <div class="role">CEO/Founder</div>
    </div>

    <div class="contact">
      <p>47 Fenwick Rd., Eldermere</p>
      <p>Northdale, CA21 4QT</p>
      <p>(01632) 960417</p>
      <p>(01632) 960538</p>
      <p>rkdbrantley@mailbox.example</p>
      <p>www.brantleyspharmacy.example</p>
    </div>

    <div class="icons">
      <svg class="icon solid" style="top:2px" viewBox="0 0 18 18" aria-label="person"><circle cx="9" cy="5" r="3.5"/><path d="M2 17c0-4 3-6.5 7-6.5s7 2.5 7 6.5z"/></svg>
      <svg class="icon" style="top:54px" viewBox="0 0 18 18" aria-label="location"><path d="M9 17s-5.5-6-5.5-9.5a5.5 5.5 0 0 1 11 0C14.5 11 9 17 9 17z"/><circle cx="9" cy="7.5" r="2"/></svg>
      <svg class="icon solid" style="top:85px" viewBox="0 0 18 18" aria-label="telephone"><path d="M4 2l3 3-1.5 2a9 9 0 0 0 5.5 5.5L13 11l3 3-2 2.5C8 16 2 10 1.5 4z"/></svg>
      <svg class="icon" style="top:104px" viewBox="0 0 18 18" aria-label="mobile"><rect x="5" y="1.5" width="8" height="15" rx="1.5"/><line x1="8" y1="14" x2="10" y2="14"/></svg>
      <svg class="icon" style="top:123px" viewBox="0 0 18 18" aria-label="email"><rect x="1.5" y="4" width="15" height="10" rx="1"/><path d="M1.5 4.5 9 10l7.5-5.5"/></svg>
      <svg class="icon" style="top:142px" viewBox="0 0 18 18" aria-label="website"><circle cx="9" cy="9" r="7"/><path d="M2 9h14M9 2c-3 4-3 10 0 14M9 2c3 4 3 10 0 14"/></svg>
    </div>
  </section>

  <section class="card card-back" aria-label="Business card back">
    <div class="back-web">www.brantleyspharmacy.example</div>
    <div class="back-brand">
      <div class="mark"></div>
      <div class="name">Brantley Apothecary</div>
      <div class="tagline">Health &amp; Gifts</div>
    </div>
  </section>

</main>
</body>
</html>
```